Feral Tundra, a 3d voxel survival video game needs a card for gaming conventions

I am the lead developer for Feral Tundra http://www.FeralTundra.example and need a business card to hand out at an indie gaming convention
The card would need to include the game name, website url, my name, position (Lead Developer), e-mail and phone number
The game is a 3d, voxel (with smooth terrain) based survival game with guns and wildlife. The main icon of the game would likely be a grizzly bear but I am willing to accept other designs too.
Attached is a media kit for the game with some images you can use but don't have to its just what little art I can provide. Anything on the website or from the video game can also be used. unrelated art can also be used.
Target Market(s)
Indie Developers/publishers at conferences
Industry/Entity Type
Games
Contact Information for Business Card
Name: Corin Wexford
Position: Lead Developer
E-mail: Gray_Lanterns@mailnest.example
Phone number: 555-372-9186
Look and feel

```html
<!DOCTYPE html>
<html lang="en">
<head>
<meta charset="utf-8">
<title>Feral Tundra – Business Card</title>
<link rel="stylesheet" href="https://fonts.googleapis.com/css2?family=Mulish:wght@700;800&display=swap">
<style>
  :root {
    --page: #ffffff;
    --gold-light: #f6d78c;
    --gold-mid: #a8853f;
    --gold-dark: #221804;
    --back-glow: #dcc796;
    --back-edge: #1c1505;
    --text-light: #ffffff;
    --icon-line: #ffffff;
    --art-dark: #0d0a04;
    --art-warm: #4a3816;
  }
  * { box-sizing: border-box; margin: 0; padding: 0; }
  html, body { width: 986px; height: 1200px; overflow: hidden; background: var(--page); }
  .canvas { position: relative; width: 986px; height: 1200px; }

  .card {
    position: absolute;
    left: 39px;
    width: 909px;
    height: 520px;
    border-radius: 0 70px 0 70px;
    overflow: hidden;
  }
  .card--front {
    top: 33px;
    background: linear-gradient(160deg, var(--gold-light) 0%, #d8b56a 30%, var(--gold-mid) 60%, var(--gold-dark) 100%);
  }
  .card--back {
    top: 626px;
    background: radial-gradient(ellipse 58% 62% at 50% 52%, var(--back-glow) 0%, #a48a55 45%, #4b3b17 75%, var(--back-edge) 100%);
  }

  .bear-art {
    position: absolute;
    background: radial-gradient(closest-side, var(--art-warm) 0%, var(--art-dark) 55%, rgba(13,10,4,0.85) 80%, rgba(13,10,4,0) 100%);
  }
  .card--front .bear-art { left: 30px; top: 6px; width: 320px; height: 275px; }
  .card--back .bear-art { left: 262px; top: 100px; width: 390px; height: 350px; }

  .game-title {
    position: absolute;
    font-family: "Mulish", Arial, sans-serif;
    font-weight: 800;
    font-size: 54px;
    line-height: 1;
    color: var(--text-light);
    white-space: nowrap;
  }
  .card--front .game-title { left: 392px; top: 60px; }
  .card--back .game-title { left: 0; right: 0; top: 26px; text-align: center; }

  .person {
    position: absolute;
    left: 0;
    width: 380px;
    top: 292px;
    text-align: center;
    color: var(--text-light);
    font-family: "Mulish", Arial, sans-serif;
  }
  .person__name { font-size: 33px; font-weight: 700; }
  .person__role { margin-top: 14px; font-size: 19px; font-weight: 800; letter-spacing: 0.5px; }

  .contacts {
    position: absolute;
    left: 404px;
    top: 222px;
    list-style: none;
    font-family: "Mulish", Arial, sans-serif;
    color: var(--text-light);
    font-weight: 700;
  }
  .contacts__item { display: flex; align-items: center; height: 60px; margin-bottom: 29px; }
  .contacts__icon { width: 56px; height: 56px; flex: none; margin-right: 2px; }
  .contacts__text { font-size: 24px; white-space: nowrap; }
  .contacts__item--phone .contacts__text { font-size: 28px; }

  .back-url {
    position: absolute;
    left: 0; right: 0;
    top: 455px;
    text-align: center;
    font-family: "Mulish", Arial, sans-serif;
    font-weight: 700;
    font-size: 29px;
    color: var(--text-light);
  }
</style>
</head>
<body>
<main class="canvas">

  <section class="card card--front" aria-label="Business card front">
    <div class="bear-art" role="img" aria-label="Roaring grizzly bear head illustration in black"></div>
    <h1 class="game-title">Feral Tundra</h1>

    <div class="person">
      <p class="person__name">Corin Wexford</p>
      <p class="person__role">LEAD DEVELOPER</p>
    </div>

    <ul class="contacts">
      <li class="contacts__item contacts__item--phone">
        <svg class="contacts__icon" viewBox="0 0 60 60" aria-hidden="true">
          <path d="M14 10 l9 -3 l7 13 l-6 5 q4 9 12 13 l5 -6 l13 7 l-3 9 q-3 4 -9 3 q-20 -5 -30 -28 q-1 -8 2 -13 z" fill="none" stroke="var(--icon-line)" stroke-width="2.5" stroke-linejoin="round"/>
          <path d="M34 10 q12 3 15 15 M34 18 q6 2 8 8" fill="none" stroke="var(--icon-line)" stroke-width="2.5" stroke-linecap="round"/>
        </svg>
        <span class="contacts__text">:555-372-9186</span>
      </li>
      <li class="contacts__item contacts__item--email">
        <svg class="contacts__icon" viewBox="0 0 60 60" aria-hidden="true">
          <rect x="3" y="14" width="54" height="34" fill="none" stroke="var(--icon-line)" stroke-width="3"/>
          <path d="M3 14 L30 35 L57 14 M3 48 L23 30 M57 48 L37 30" fill="none" stroke="var(--icon-line)" stroke-width="3"/>
        </svg>
        <span class="contacts__text">:Gray_Lanterns@mailnest.example</span>
      </li>
      <li class="contacts__item contacts__item--web">
        <svg class="contacts__icon" viewBox="0 0 60 60" aria-hidden="true">
          <g fill="none" stroke="var(--icon-line)" stroke-width="2.2">
            <circle cx="30" cy="30" r="25"/>
            <ellipse cx="30" cy="30" rx="11" ry="25"/>
            <line x1="30" y1="5" x2="30" y2="55"/>
            <line x1="5" y1="30" x2="55" y2="30"/>
            <path d="M9 17 H51 M9 43 H51"/>
          </g>
        </svg>
        <span class="contacts__text">:www.feraltundra.example</span>
      </li>
    </ul>
  </section>

  <section class="card card--back" aria-label="Business card back">
    <h2 class="game-title">Feral Tundra</h2>
    <div class="bear-art" role="img" aria-label="Large roaring grizzly bear head illustration in black"></div>
    <p class="back-url">www.feraltundra.example</p>
  </section>

</main>
</body>
</html>
```